Ringwell Lookup - Web design / template design

Hello,

I need a design for my existing site. I already have a logo that I want to use, which you can find on my site ( I can also provide different formats / larger versions ).

Please see http://www.ringwelllookup.example for details of the site.

What I need are pages with sections that can be edited, so for example, I need basic table / div content sections that I can place in the members area that can contain whatever custom content I need to put in them without the table / div design getting stretched out or skewed.

The main page, basically needs to have all of the content on the current page or room for it at least should I want to add it.

You can also see ww2.ringwelllookup.example with more info ( not a live site and me trying my best to do something, but I'm just not good at design :)

The site content for the most part needs to be actual text, rather than text on images. I will need to change this content and have it indexed by search engines, if you want, you can just put filler text in. There are exceptions of course, like maybe on the main page, if there are boxes with some static image text, that is fine.

Target Market(s)

Telephony, phone service providers, phone system users

Industry/Entity Type

It Service

Requirements
Must have
• Dynamic content capabilities.

Logo colors implemented in the site in some way.

Easy navigation ( tabs at the top are good or whatever you think ).

I will have the following sections:

1. Home
2. About us ( company info ).
3. How to / Help
4. Pricing
5. Support section.
6. Contact section
7. Singup section
8. Members section

I would like the main page to be more image / wow factor and the other pages really just need to be basic layout and places to put tables or divs with content in them. Table or div header images are for titles are ok as long as I can edit them.

Nice to have
• Sign up button placed somewhere.

Twitter / Facebook / LinkedIn buttons

Should not have
• Flash or all page content in static images.

```html
<!DOCTYPE html>
<html lang="en">
<head>
<meta charset="utf-8">
<title>Ringwell Lookup</title>
<link rel="stylesheet" href="https://fonts.googleapis.com/css2?family=Arimo:wght@400;700&display=swap">
<style>
:root{
  --blue:#3a8ee8;
  --blue-dark:#2470cf;
  --blue-light:#4aa0f2;
  --green:#52b51a;
  --green-dark:#3c9a0c;
  --ink:#222;
  --muted:#666;
  --rule:#d8d8d8;
  --page:#f4f4f4;
  --link:#1a6fc4;
}
*{box-sizing:border-box;margin:0;padding:0}
html,body{width:1200px;height:1200px;overflow:hidden;background:var(--page)}
body{font-family:"Arimo",Arial,sans-serif;color:var(--ink)}
.stage{width:1400px;height:1400px;transform:scale(.857143);transform-origin:0 0;position:relative;background:var(--page)}
.abs{position:absolute}

.topbar{left:0;top:0;width:1400px;height:30px;background:linear-gradient(#4aa3f5,#2f86e4);color:#fff;font-size:11px}
.topbar .find{left:215px;top:8px}
.social{left:287px;top:6px;display:flex;gap:7px}
.social span{width:16px;height:16px;border-radius:3px;background:#fff;opacity:.85}
.social span.rss{background:#f39a2b;opacity:1}
.topbar .support{right:222px;top:8px}
.topbar .support b{font-weight:400;color:#ffd34d}

.header{left:0;top:30px;width:1400px;height:655px;background:radial-gradient(ellipse 420px 110px at 760px 40px,#fff,transparent),linear-gradient(#e6e6e6 0,#f4f4f4 130px,#f4f4f4)}
.brand{left:243px;top:70px;display:flex;align-items:center;gap:10px;font-size:34px;color:var(--blue-dark)}
.brand i{width:14px;height:14px;border-radius:50%;background:var(--green)}
.nav{left:222px;top:118px;width:956px;height:44px;background:linear-gradient(#fff,#f4f4f4);border-radius:26px 26px 0 0;border-top:1px solid #e2e2e2}
.nav a{position:absolute;top:17px;font-size:14px;color:#333;text-decoration:none}
.nav a.active{left:20px;top:9px;width:105px;height:30px;line-height:30px;text-align:center;color:#fff;border-radius:6px;background:linear-gradient(#6fd232,#3c9e0c)}
.hero{left:219px;top:206px;width:960px;height:400px;background:linear-gradient(90deg,#e8c3a8 0,#f2d8c6 45%,#fafafa 58%,#fff 100%)}
.hero-shadow{left:240px;top:606px;width:920px;height:30px;background:radial-gradient(ellipse at 50% 0,rgba(0,0,0,.9),rgba(0,0,0,.25) 55%,transparent 75%)}

.content{left:0;top:685px;width:1400px;height:405px;background:#fff;border-top:1px solid #e6e6e6}
.col h3{font-size:14px;letter-spacing:.3px}
.col .sub{font-size:11px;color:var(--muted);margin-top:4px;padding-bottom:10px;border-bottom:1px solid var(--rule)}
.col p{font-size:11px;line-height:20px;color:#444}
.col p a{color:var(--link)}
.frame{border:1px solid #ddd;padding:5px;background:#fff;margin:11px 0 17px}
.frame div{height:81px}
.btn{display:inline-block;margin-top:12px;height:22px;line-height:22px;padding:0 10px;font-size:11px;color:#fff;background:linear-gradient(#6fd232,#3c9e0c);border:1px solid var(--green-dark)}

table.q{border-collapse:collapse;font-size:11px;text-align:center}
table.q th{font-size:14px;letter-spacing:.5px;height:40px}
table.q td{height:19px}
table.light{width:317px;color:#999}
table.light th,table.light td{border:1px solid #d4d4d4}
table.light td{border-top:2px solid #e0e0e0}
table.dark{width:317px;color:#fff}
table.dark th,table.dark td{border:1px solid #cfe3fb}
table.dark td{height:19.4px}

.band{left:0;top:1090px;width:1400px;height:63px;background:linear-gradient(#e4e4e4,#d8d8d8);border-top:1px solid #999}
.band h4{position:absolute;left:218px;top:16px;font-size:12px;color:#3a1a05}
.band p{position:absolute;left:218px;top:34px;font-size:11px;color:var(--muted)}
.signup{left:1012px;top:12px;width:162px;height:41px;line-height:41px;text-align:center;font-size:24px;color:#fff;border-radius:4px;background:linear-gradient(#76d83a,#3c9e0c);border:1px solid var(--green-dark)}

.footer{left:0;top:1153px;width:1400px;height:247px;background:linear-gradient(var(--blue-light),var(--blue) 40%,var(--blue-dark));border-top:3px solid #1c62bd;color:#fff}
.fcol{top:27px}
.fcol h5{font-size:14px;letter-spacing:.4px;margin-bottom:18px;color:#e8f2ff}
.fcol li{list-style:none;font-size:11px;line-height:20px}
.frule{left:219px;top:188px;width:960px;border-top:1px solid #2a6cc2;box-shadow:0 1px 0 #5aa6f2}
.copy{left:219px;top:209px;font-size:11px;color:#a9cdf5}
.copy b{color:#dbeaff;margin-left:12px}
</style>
</head>
<body>
<div class="stage">
  <div class="abs topbar">
    <span class="abs find">Find us on:</span>
    <div class="abs social"><span></span><span></span><span></span><span></span><span class="rss"></span></div>
    <span class="abs support">Click here to live Support &nbsp;Tell Free <b>1-555-010-2030</b></span>
  </div>

  <div class="abs header">
    <div class="abs brand" style="top:40px"><i></i>Ringwell Lookup</div>
    <nav class="abs nav" style="top:88px">
      <a class="active" href="#">Home</a>
      <a href="#" style="left:183px">Services</a>
      <a href="#" style="left:321px">Pricing</a>
      <a href="#" style="left:444px">Support</a>
      <a href="#" style="left:566px">Contact Us</a>
    </nav>
  </div>
  <div class="abs hero" role="img" aria-label="Photo of a support agent wearing a headset"></div>
  <div class="abs hero-shadow"></div>

  <div class="abs content">
    <div class="abs col" style="left:219px;top:53px;width:285px">
      <h3>Low Rates</h3>
      <div class="sub">Lorem ipsum dolor sit amet, consectetur adipisicing elit</div>
      <div class="frame"><div role="img" aria-label="Illustration of a green dollar sign" style="background:linear-gradient(90deg,#fff,#e4f3d8 40%,#cfe9b8 55%,#fff)"></div></div>
      <p><a href="#">Lorem ipsum dolor sit amet</a>, consectetur adipisi cing elit, sed do eiusmod tempor incididunt ut labore et dolore magna aliqua. Ut enim ad minim veniam, quisnostrud exercitation ullamco laboris nisi ut aliquip.</p>
      <span class="btn">Read More »</span>
    </div>

    <div class="abs col" style="left:555px;top:53px;width:285px">
      <h3 style="font-size:12px">Recent Query Results:</h3>
      <div class="sub">Lorem ipsum dolor sit amet, consectetur adipisicing elit</div>
    </div>
    <table class="abs q light" style="left:540px;top:108px">
      <tr><th>Phone Number</th><th>Caller ID name</th></tr>
      <tr><td>425765XXXX</td><td>XXX Phone XXX</td></tr>
      <tr><td>425765XXXX</td><td>XXX Phone XXX</td></tr>
      <tr><td>425765XXXX</td><td>XXX Phone XXX</td></tr>
      <tr><td>425765XXXX</td><td>XXX Phone XXX</td></tr>
      <tr><td>425765XXXX</td><td>XXX Phone XXX</td></tr>
      <tr><td>425765XXXX</td><td>XXX Phone XXX</td></tr>
      <tr><td>425765XXXX</td><td>XXX Phone XXX</td></tr>
      <tr><td>425765XXXX</td><td>XXX Phone XXX</td></tr>
      <tr><td>425765XXXX</td><td>XXX Phone XXX</td></tr>
      <tr><td>425765XXXX</td><td>XXX Phone XXX</td></tr>
    </table>

    <div class="abs col" style="left:889px;top:53px;width:285px">
      <h3>CNAM How To</h3>
      <div class="sub">Lorem ipsum dolor sit amet, consectetur adipisicing elit</div>
      <div class="frame"><div role="img" aria-label="Close-up photo of a telephone caller ID button" style="background:linear-gradient(135deg,#3a2a1c,#6b4c30 50%,#4a3522)"></div></div>
      <p>Mauris interdum velit lacus, sit amet rutrum augue. Morbi sit amet viverra massa. Maecenas felis mi, lobortis ut elementum vitae, placerat a justo. Aliquam quis mauris justo. Curabitur vel dolor et quam imperdiet fermentum.</p>
      <span class="btn">Read More »</span>
    </div>
  </div>

  <div class="abs band">
    <h4>Welcome to Ringwell Lookup:</h4>
    <p>Donec metus lacus, porta id, auctor sit amet, aliquam eu, lacus. Quisque sagittis vulputate orci.</p>
    <div class="abs signup">Singup Now</div>
  </div>

  <footer class="abs footer">
    <div class="abs fcol" style="left:219px"><h5>About</h5><ul><li>Overview</li><li>Another Link</li><li>Our Company</li><li>Our Staff</li><li>Mission Statement</li></ul></div>
    <div class="abs fcol" style="left:392px"><h5>Services</h5><ul><li>First Service</li><li>Second Service</li><li>Another Service</li><li>A Fourth Service</li></ul></div>
    <div class="abs fcol" style="left:567px"><h5>Join for free</h5><ul><li>Image Gallery</li><li>Video Gallery</li><li>Audio Files</li><li>The Podcast</li></ul></div>
    <div class="abs fcol" style="left:725px"><h5>Pricing</h5><ul><li>Category One</li><li>Category 2</li><li>Another Category</li><li>Category</li><li>A Fifth Category</li></ul></div>
    <table class="abs q dark" style="left:866px;top:4px">
      <tr><th>Phone Number</th><th>Caller ID name</th></tr>
      <tr><td>425765XXXX</td><td>XXX Phone XXX</td></tr>
      <tr><td>425765XXXX</td><td>XXX Phone XXX</td></tr>
      <tr><td>425765XXXX</td><td>XXX Phone XXX</td></tr>
      <tr><td>425765XXXX</td><td>XXX Phone XXX</td></tr>
      <tr><td>425765XXXX</td><td>XXX Phone XXX</td></tr>
      <tr><td>425765XXXX</td><td>XXX Phone XXX</td></tr>
      <tr><td>425765XXXX</td><td>XXX Phone XXX</td></tr>
    </table>
    <div class="abs frule"></div>
    <div class="abs copy">© Copyright ringwelllookup . All Rights Reserved. <b>Home | Contact | RSS</b></div>
  </footer>
</div>
</body>
</html>
```